a small documentary making company needs a fancy simple website

Hi

Need a Website that is classic and funky at the same time

I have a simple design already made up but need some advice and someone to give it that wow factor.

the structure should be simple, my proposition is:

Home Page:
* Home
* Store
** Purchase (Trailer Preview / Desc / Info)
** (Purchase options: Buy DVD / Rent/View 48 Hrs)
* Portfolio
** Who we are
** Projects
** Media Presence
* Contact

I have the logo and proposed design, our launch date is 13/05/2012 so we need this site developed / up and running in two weeks.

this job is for a design + code

Faithfully
Leopold

Target Market(s)

Spiritual and Religious

Industry/Entity Type

It Company

Requirements
Must have
• * Ability to sell dvd's
* Google & Bing search friendly
* Play video Trailers
Nice to have
• Flash Interface

```html
<!DOCTYPE html>
<html lang="en">
<head>
<meta charset="utf-8">
<title>Vox Lumen Pictures</title>
<link href="https://fonts.googleapis.com/css2?family=Ubuntu:wght@400;500;700&family=Arimo:wght@400;700&display=swap" rel="stylesheet">
<style>
:root{
  --brown-top:#2a2118;
  --brown-mid:#3a2d20;
  --brown-dark:#15110d;
  --red-light:#e23b3b;
  --red:#cc1414;
  --red-dark:#a80c0c;
  --cart-count:#ff3a3a;
  --white:#ffffff;
  --text-gray:#7a7a7a;
  --text-dark:#2b2b2b;
  --hall-warm:#8a6a42;
  --hall-dark:#2a2016;
}
*{margin:0;padding:0;box-sizing:border-box}
html,body{width:1200px;height:1021px;overflow:hidden}
body{position:relative;background:#fff;font-family:"Arimo",Arial,sans-serif;color:var(--text-dark)}
.abs{position:absolute}

.site-header{left:0;top:0;width:1200px;height:108px;background:linear-gradient(180deg,#120e0a 0%,var(--brown-top) 60%,var(--brown-mid) 100%)}
.brand{left:174px;top:30px;font-family:"Ubuntu",sans-serif;font-weight:400;font-size:30px;color:var(--white);letter-spacing:1px;display:flex;align-items:center;gap:10px}
.brand-mark{width:22px;height:22px;border-radius:50%;background:var(--white)}
.brand-sub{left:174px;top:72px;font-family:"Ubuntu",sans-serif;font-size:12px;color:#e9e2d8;letter-spacing:2px}

.main-nav{left:0;top:108px;width:1200px;height:38px;background:linear-gradient(180deg,var(--red-light) 0%,var(--red) 55%,var(--red-dark) 100%)}
.nav-sep{top:0;width:1px;height:38px;background:rgba(120,0,0,.55);box-shadow:1px 0 0 rgba(255,120,120,.35)}
.nav-link{top:0;height:38px;line-height:38px;font-family:"Ubuntu",sans-serif;font-size:13.5px;color:var(--white);text-align:center;transform:translateX(-50%);white-space:nowrap}
.cart-icon{left:797px;top:5px;width:24px;height:24px;border-radius:50%;background:var(--white);box-shadow:0 0 0 2px rgba(255,255,255,.3)}
.cart-text{left:827px;top:0;height:38px;line-height:38px;font-size:9.5px;font-weight:700;color:var(--white)}
.cart-text b{color:var(--cart-count)}

.hero-side{top:146px;height:441px;width:171px;background:linear-gradient(180deg,#cfc8c0 0%,#e4ded8 35%,#d8d2cc 70%,#c9c6c3 100%);opacity:.95}
.hero-photo{left:171px;top:146px;width:860px;height:441px;border:2px solid var(--white);border-top:0;
  background:radial-gradient(ellipse at 60% 30%,#c9a978 0%,rgba(160,120,75,.8) 20%,transparent 55%),
  linear-gradient(180deg,#3a2c1e 0%,var(--hall-warm) 40%,#5b4630 70%,var(--hall-dark) 100%)}
.welcome{left:194px;top:177px;width:303px;height:300px;background:rgba(50,44,40,.6)}
.welcome h1{font-family:"Ubuntu",sans-serif;font-weight:500;font-size:27px;line-height:31px;color:var(--white);text-align:center;padding-top:6px;height:74px;border-bottom:1px solid rgba(255,255,255,.18)}
.welcome p{font-size:9.4px;line-height:15.3px;color:var(--white);padding:0 18px 0 13px}
.welcome .intro{margin-top:7px}
.welcome .gap{margin-top:15.3px}
.btn-more{left:207px;top:446px;width:101px;height:25px;border-radius:13px;background:linear-gradient(180deg,#e6e6e6,#9c9c9c);font-family:"Ubuntu",sans-serif;font-size:12px;color:var(--white);text-align:center;line-height:25px}

.content{left:170px;top:587px;width:861px;height:254px;background:var(--white);box-shadow:0 0 3px rgba(0,0,0,.08)}
.section-title{font-family:"Ubuntu",sans-serif;font-weight:400;font-size:17.5px;color:var(--text-dark)}
.dvd-box{left:194px;top:634px;width:80px;height:91px;background:linear-gradient(135deg,#c9a24a,#6a4a2a 60%,#2a1c14)}
.film-area{left:488px;top:587px;width:152px;height:106px;background:radial-gradient(ellipse at 40% 40%,#d6d6d6 0%,#ececec 45%,rgba(255,255,255,0) 75%)}
.product-title{left:284px;top:632px;font-size:12.5px;color:var(--text-dark)}
.product-title b{font-weight:400}
.product-title span{font-size:12px}
.product-desc{left:284px;top:648px;width:195px;font-size:9.3px;line-height:15.3px;color:var(--text-gray)}
.btn-buy{left:285px;top:807px;width:78px;height:24px;border-radius:12px;background:linear-gradient(180deg,var(--red-light),var(--red-dark));font-family:"Ubuntu",sans-serif;font-weight:700;font-size:10.5px;color:var(--white);text-align:center;line-height:24px;letter-spacing:.5px}
.price{left:373px;top:809px;font-family:"Ubuntu",sans-serif;font-size:16px;color:var(--text-gray);text-decoration:underline}
.video{left:669px;top:635px;width:345px;height:189px;background:#050607}
.video-frame{left:0;top:22px;width:345px;height:150px;background:linear-gradient(180deg,#5e6a78 0%,#9aa3ad 35%,#3a3e44 65%,#08090a 100%)}
.video-bar{left:0;top:174px;width:345px;height:15px;background:linear-gradient(180deg,#2b2b2b,#111)}
.video-progress{left:0;top:172px;width:345px;height:2px;background:#444}
.video-progress i{position:absolute;left:0;top:0;width:100px;height:2px;background:var(--red)}
.video-time{left:53px;top:177px;font-size:6px;color:#cfcfcf}

.site-footer{left:0;top:841px;width:1200px;height:180px;background:linear-gradient(180deg,var(--brown-mid) 0%,#1e1811 35%,var(--brown-dark) 100%)}
.footer-nav{left:183px;top:859px;font-size:9.5px;color:var(--white);display:flex;white-space:nowrap}
.footer-nav span{padding:0 7px}
.footer-nav span:first-child{padding-left:0}
.footer-nav .sep{padding:0 6px}
.footer-nav .current{text-decoration:underline}
.social{top:857px;width:14px;height:14px;border-radius:2px}
.copyright{right:179px;top:860px;font-size:9.5px;color:var(--white)}
</style>
</head>
<body>

<header class="site-header abs">
  <div class="brand abs"><span class="brand-mark"></span>Vox Lumen Pictures</div>
  <div class="brand-sub abs">voxlumenpictures.com</div>
</header>

<nav class="main-nav abs">
  <div class="nav-sep abs" style="left:169px"></div>
  <div class="nav-sep abs" style="left:281px"></div>
  <div class="nav-sep abs" style="left:393px"></div>
  <div class="nav-sep abs" style="left:499px"></div>
  <div class="nav-sep abs" style="left:638px"></div>
  <div class="nav-sep abs" style="left:778px"></div>
  <div class="nav-sep abs" style="left:1031px"></div>
  <a class="nav-link abs" style="left:225px">Home</a>
  <a class="nav-link abs" style="left:337px">Stores</a>
  <a class="nav-link abs" style="left:446px">Press</a>
  <a class="nav-link abs" style="left:568px">Philosophy</a>
  <a class="nav-link abs" style="left:708px">Contact Us</a>
  <svg class="cart-icon abs" viewBox="0 0 24 24" aria-hidden="true">
    <path d="M6 10h12l-1.5 7h-9z" fill="#cc1414"/>
    <path d="M9 10l3-4 3 4" fill="none" stroke="#cc1414" stroke-width="1.4"/>
  </svg>
  <div class="cart-text abs">You have <b>0</b> items</div>
</nav>

<div class="hero-side abs" style="left:0" role="img" aria-label="Faded cloister corridor photograph"></div>
<div class="hero-side abs" style="left:1031px;width:169px" role="img" aria-label="Faded cloister corridor photograph"></div>
<div class="hero-photo abs" role="img" aria-label="Gothic cloister with sunlight through arched windows"></div>

<section class="welcome abs">
  <h1>Welcome to our<br>website !</h1>
  <p class="intro">But I must explain to you how all this mistaken idea of denouncing pleasure and praising pain was born and I will give you a complete account of the system, and expound the actual teach-ings of the great explorer of the truth, the master-builder of human happiness.</p>
  <p class="gap">No one rejects, dislikes, or avoids pleasure itself, because it is pleasure, but because those who do not know how to pursue pleasure rationally encounter consequences that are extremely painful.</p>
  <p>Nor again is there anyone who loves or pursues or desires to obtain pain of itself, because it is pain</p>
</section>
<a class="btn-more abs">Read more</a>

<main class="content abs"></main>
<div class="film-area abs" role="img" aria-label="Curling film strip illustration"></div>
<h2 class="section-title abs" style="left:209px;top:606px">Our Products</h2>
<div class="dvd-box abs" role="img" aria-label="DVD box set cover"></div>
<div class="product-title abs"><b>Vox Lumen 1 Series</b> <span>on DVD</span></div>
<p class="product-desc abs">On the other hand, we denounce with righ-teous indignation and dislike men who are so beguiled and demoralized by the charms of pleasure of the moment, so blinded by desire, that they cannot foresee the pain and trouble that are bound to ensue<br>"On the other hand, we denounce with righ-teous indignation and dislike men who are so beguiled and demoralized by the charms of pleasure of the moment, so blinded by desire,</p>
<a class="btn-buy abs">Buy now</a>
<div class="price abs">$ 12,99</div>

<h2 class="section-title abs" style="left:666px;top:606px">Videos</h2>
<div class="video abs">
  <div class="video-frame abs" role="img" aria-label="Video still of mountain peaks above clouds with a monastery"></div>
  <div class="video-progress abs"><i></i></div>
  <div class="video-bar abs"></div>
  <svg class="abs" style="left:12px;top:178px" width="40" height="8" viewBox="0 0 40 8" aria-hidden="true">
    <rect x="0" y="1" width="2" height="6" fill="#ccc"/><rect x="4" y="1" width="2" height="6" fill="#ccc"/>
    <path d="M22 3h2l3-2v6l-3-2h-2z" fill="#ccc"/>
  </svg>
  <div class="video-time abs">0:22 / 1:19</div>
</div>

<footer class="site-footer abs"></footer>
<div class="footer-nav abs">
  <span>Home</span><span class="sep">|</span><span>Stores</span><span class="sep">|</span><span>Press</span><span class="sep">|</span><span class="current">Philosophy</span><span class="sep">|</span><span>Contact Us</span><span class="sep">|</span>
</div>
<div class="social abs" style="left:492px;background:#3b5998"></div>
<div class="social abs" style="left:515px;background:#3fb3e3"></div>
<div class="copyright abs">All right reserved. Copyright 2012 Vox Lumen Pictures Ltd.</div>

</body>
</html>
```